label for selfmade spirits, start-up, quality product

Hey there, my name is Tobias, I am 24 years old, living in the southwest of Germany. In the last two years I did experiment: I produced my own spirits. I used self-produced fruit and distilled it in my families small distillery. Distilling has been a tradition in my family, now I want to start my own production and sales. In our region distilling fruit is a tradition but it is in the hand of well-established families / producers. I am planning to establish a quality product with a modern design to focus more on younger people and to sell my spirits to bars, restaurants and private consumers. I did two varieties: "Jojo plum variety" and "Mirabelle de Nancy". (Mirabelle) I am looking for a label design. The bottles will have 0.7 liters, white glass (due to the clear color of the spirits), in a modern bottle: https://www.glasbruckhaus-beispiel.de/flaschen-und-glaeser/spirituosen/spirituosenflaschen/varna-417 , html taste: clear and noble fruit character in the nose, fine flavor of the respective fruit. During the distillation process I tried to capture the natural aroma of the fruit. Therefore, I did a 2nd distilation which is a special feature, that not everybody does. Jojo Zwetschgen Brand "/" Mirabelle de Nancy Brand "- I am also open for. The design can be: - simple and classy, ​​with a valuable appearance that shows in its font, which is the product itself 3 generations were involved in the production, my grandpa gave me important hints, .. I am so open for all ideas that could catch the target group. the label could be printed on either a white or cream label paper. If you have any questions don`t hesitate to contact me, I am looking forward to your suggestions! Cheers!

Target Market(s)

young adults, urban people, people with an interest in a high quality product, ars / restaurants / private customers

Font styles to use
Decorative
Script

Colors

Designer to choose colors to be used in the design.

Requirements
Must have
• So, there are some things that have been posted on the label, due to legal restrictions: - my address: Tobias Wernsdorfer, Lindenweg 14, 68412 Rebhausen - alcohol level: "alc. 42% vol." - capacity: "0.70 L"; size at least 4 mm - batch number: "L"; please leave an empty space to fill in by hand this information has not been discussed, but should not be too much in the foreground, nor attract to much attention.

```html
<!DOCTYPE html>
<html lang="en">
<head>
<meta charset="utf-8">
<title>Noro Zwetschge Brand – Label Set</title>
<link href="https://fonts.googleapis.com/css2?family=Roboto+Condensed:wght@400;700&family=Open+Sans:wght@400;600&display=swap" rel="stylesheet">
<style>
  :root {
    --bg-outer: #9c9c9c;
    --bg-inner: #d4d4d4;
    --paper: #ecebeb;
    --paper-shade: #dcdbdb;
    --ink: #2b2b2d;
    --ink-soft: #7b7b7e;
    --band-dark: #1f1d1f;
    --band-text: #f2f2f2;
    --wave-light: #c4c4c6;
    --wave-mid: #a9a9ab;
    --orchard-green: #6f8358;
    --orchard-blossom: #e3e6df;
    --orchard-sky: #a8c3d8;
  }
  * { box-sizing: border-box; margin: 0; padding: 0; }
  html, body { width: 1200px; height: 1200px; overflow: hidden; }
  body {
    background: radial-gradient(ellipse at 50% 45%, var(--bg-inner) 0%, var(--bg-outer) 100%);
    position: relative;
    font-family: "Open Sans", sans-serif;
  }
  .label {
    position: absolute;
    top: 385px;
    width: 520px;
    height: 430px;
    background: linear-gradient(180deg, var(--paper) 0%, var(--paper-shade) 100%);
    overflow: hidden;
    box-shadow: 0 6px 18px rgba(0,0,0,0.18);
  }
  .label--front { left: 40px; }
  .label--back { left: 640px; }

  .orchard-band {
    position: absolute; left: 0; top: 0; width: 100%; height: 125px;
    background: linear-gradient(180deg, var(--orchard-sky) 0%, var(--orchard-blossom) 30%, var(--orchard-blossom) 55%, var(--orchard-green) 100%);
  }

  .product-name {
    position: absolute; left: 0; width: 100%;
    text-align: center;
    font-family: "Open Sans", sans-serif;
    font-weight: 400;
    color: var(--ink);
    line-height: 1.1;
  }
  .product-name__sub {
    display: block;
    font-size: 17px;
    letter-spacing: 6px;
    color: var(--ink-soft);
    margin-top: 4px;
  }
  .label--front .product-name { top: 168px; font-size: 48px; }
  .label--front .product-name__sub { padding-left: 120px; }
  .label--back .product-name { top: 62px; font-size: 36px; }
  .label--back .product-name__sub { font-size: 13px; padding-left: 90px; margin-top: 2px; }

  .front-swoosh { position: absolute; left: 0; bottom: 0; width: 100%; height: 110px; }
  .capacity {
    position: absolute; right: 30px; bottom: 14px;
    color: var(--band-text);
    font-size: 19px;
    letter-spacing: 2px;
    font-variant: small-caps;
  }

  .producer {
    position: absolute; top: 150px; left: 0; width: 100%;
    text-align: center;
    font-family: "Roboto Condensed", sans-serif;
    font-size: 18px;
    color: var(--ink);
  }
  .legal {
    position: absolute; top: 222px; left: 92px;
    font-weight: 600;
    font-size: 14px;
    line-height: 1.45;
    color: var(--ink);
    list-style: none;
    text-align: right;
  }
  .back-waves { position: absolute; left: 0; bottom: 0; width: 100%; height: 110px; }
</style>
</head>
<body>

<section class="label label--front">
  <div class="orchard-band" role="img" aria-label="Photo of a blossoming fruit orchard with rows of trees"></div>
  <h1 class="product-name">Noro Zwetschge<span class="product-name__sub">BRAND</span></h1>
  <svg class="front-swoosh" viewBox="0 0 520 110" preserveAspectRatio="none" aria-hidden="true">
    <path d="M0 0 C120 40 170 75 260 70 C360 62 440 50 520 52 L520 110 L0 110 Z" fill="var(--band-dark)"/>
  </svg>
  <p class="capacity">0.7 Liters</p>
</section>

<section class="label label--back">
  <h2 class="product-name">Noro Zwetschge<span class="product-name__sub">BRAND</span></h2>
  <p class="producer">Hausbrennerei, Tobias Wernsdorfer, D- 68412 Rebhausen</p>
  <ul class="legal">
    <li>alcohol level:“alc. 42% vol.”</li>
    <li>capacity: “700 ml”; size at least 4 mm</li>
    <li>batch number: “L”</li>
  </ul>
  <svg class="back-waves" viewBox="0 0 520 110" preserveAspectRatio="none" aria-hidden="true">
    <path d="M0 70 C120 20 260 10 520 25 L520 110 L0 110 Z" fill="var(--wave-light)"/>
    <path d="M0 90 C140 55 300 50 520 60 L520 110 L0 110 Z" fill="var(--wave-mid)"/>
  </svg>
</section>

</body>
</html>
```